Dog grooming business card
This is a business card for m dog grooming business like it say above.
In the priorities box below I will have the text that I want on the card.

Industry/Entity Type

Business

Colors

Designer to choose colors to be used in the design.

Requirements
Must have
• My logo and the insurance stamp must be on the card.

Text it must have :

Professional grooming services
Email: lindomerfield@brightmail.example
Text or call 1 705 318 6052
KSR certified/member
Pet first aid certified
Next appointment ___________________________________
Nice to have
• Greens to match my logo

```html
<!DOCTYPE html>
<html lang="en">
<head>
<meta charset="utf-8">
<title>Lindo Merfield – Professional grooming services business card</title>
<link rel="stylesheet" href="https://fonts.googleapis.com/css2?family=Arimo:wght@400;700&family=Fondamento&display=swap">
<style>
  :root {
    --stage: #efeee9;
    --card-white: #ffffff;
    --leaf: #9dc74a;
    --leaf-light: #a9cf56;
    --leaf-deep: #7aa334;
    --ink: #222222;
    --rule: #3a3a3a;
    --badge-blue: #3f7fc4;
    --shadow: rgba(0,0,0,0.18);
  }
  * { box-sizing: border-box; margin: 0; padding: 0; }
  html, body { width: 1200px; height: 914px; overflow: hidden; }
  body {
    background: var(--stage);
    font-family: "Arimo", Arial, sans-serif;
    color: var(--ink);
    position: relative;
  }
  .card {
    position: absolute;
    left: 250px;
    width: 700px;
    height: 400px;
    box-shadow: 0 6px 18px var(--shadow);
    overflow: hidden;
  }
  /* Front side */
  .card-front { top: 47px; background: var(--card-white); }
  .brand {
    position: absolute;
    left: 40px; top: 48px;
    display: flex; align-items: center; gap: 12px;
  }
  .brand-dot {
    width: 38px; height: 38px; border-radius: 50%;
    background: var(--leaf);
  }
  .brand-name {
    font-family: "Fondamento", cursive;
    font-size: 34px;
    color: var(--ink);
  }
  .credentials {
    position: absolute;
    right: 50px; top: 96px;
    font-weight: 700;
  }
  .credentials .first-aid { font-size: 19px; }
  .credentials .membership { font-size: 16px; margin-top: 3px; }
  .info-band {
    position: absolute;
    left: 0; right: 0; top: 168px; height: 164px;
    background: var(--leaf-light);
    border-top: 3px solid var(--rule);
    border-bottom: 3px solid var(--rule);
  }
  .contact-line {
    position: absolute; left: 40px; top: 14px;
    font-size: 15px; color: var(--ink);
  }
  .contact-line .phone { color: #fff; margin-left: 6px; }
  .appointment-label {
    position: absolute; left: 40px; top: 44px;
    font-size: 17px; font-weight: 700;
  }
  .appointment-box {
    position: absolute; left: 40px; top: 72px;
    width: 500px; height: 60px;
    background: var(--card-white);
  }
  .insurance-badge {
    position: absolute; right: 40px; top: 62px;
    width: 110px; height: 62px;
    border-radius: 10px;
    background: var(--card-white);
    border: 3px solid var(--badge-blue);
  }
  .bottom-rule {
    position: absolute; left: 0; right: 0; top: 368px;
    height: 2px; background: var(--rule);
  }
  /* Back side */
  .card-back {
    top: 467px;
    background: linear-gradient(135deg, var(--leaf-light), var(--leaf));
  }
  .back-emblem {
    position: absolute; left: 250px; top: 50px;
    width: 200px; height: 110px;
  }
  .back-brand {
    position: absolute; left: 0; right: 0; top: 168px;
    display: flex; justify-content: center; align-items: center; gap: 12px;
  }
  .back-brand .brand-dot { background: var(--leaf-deep); }
  .back-brand .brand-name { font-size: 44px; }
  .tagline {
    position: absolute; left: 0; right: 0; top: 250px;
    text-align: center;
    font-family: "Fondamento", cursive;
    font-size: 32px; color: var(--ink);
  }
</style>
</head>
<body>
  <section class="card card-front">
    <div class="brand">
      <span class="brand-dot"></span>
      <span class="brand-name">Lindo Merfield</span>
    </div>
    <div class="credentials">
      <p class="first-aid">Pet first aid certified</p>
      <p class="membership">KSR certified/member</p>
    </div>
    <div class="info-band">
      <p class="contact-line">lindomerfield@brightmail.example <span class="phone">Text or call 1 705 318 6052</span></p>
      <p class="appointment-label">Next appointment</p>
      <div class="appointment-box"></div>
      <div class="insurance-badge" role="img" aria-label="Insurance protection badge"></div>
    </div>
    <div class="bottom-rule"></div>
  </section>

  <section class="card card-back">
    <svg class="back-emblem" viewBox="0 0 200 110" role="img" aria-label="Faint grooming emblem area">
      <rect x="0" y="0" width="200" height="110" rx="40" fill="#93bd45" opacity="0.6"/>
    </svg>
    <div class="back-brand">
      <span class="brand-dot"></span>
      <span class="brand-name">Lindo Merfield</span>
    </div>
    <p class="tagline">Professional grooming services</p>
  </section>
</body>
</html>
```